Business Card Design Project

I need a business card for an environmentally friendly interior design company called Roomcraft Willow.
I was thinking it might be nice to print the business cards on brown recycled paper with green ink.
In addition to interior design, I will also be able to consult with homeowners regarding their indoor environments and how they might be affecting their health after May 2013 which is when I will complete my certification program. This can be added to the business card at that time: "Certified Habitat Vitalis Dwelling Consultant".
Health

```html
<!DOCTYPE html>
<html lang="en">
<head>
<meta charset="utf-8">
<title>Roomcraft Willow – Business Card</title>
<link href="https://fonts.googleapis.com/css2?family=Marcellus&family=Alegreya:wght@400;500&display=swap" rel="stylesheet">
<style>
  :root {
    --backdrop: #ededed;
    --bark: #4a3326;
    --leaf: #8cc63f;
    --mist-light: #f4f4f4;
    --mist-dark: #d9d9d9;
    --faint: rgba(255, 255, 255, 0.12);
  }
  * { box-sizing: border-box; margin: 0; padding: 0; }
  html, body { width: 1200px; height: 795px; overflow: hidden; }
  body {
    background: var(--backdrop);
    display: flex;
    align-items: center;
    justify-content: center;
    gap: 60px;
    font-family: "Alegreya", Georgia, serif;
  }
  .card {
    width: 490px;
    height: 280px;
    position: relative;
    overflow: hidden;
    box-shadow: 0 6px 18px rgba(0,0,0,0.12);
  }

  /* Front face */
  .card-front { background: var(--bark); }
  .front-band {
    position: absolute; inset: 0 0 auto 0;
    height: 92px;
    background: linear-gradient(180deg, var(--mist-light), var(--mist-dark));
    display: flex; align-items: center; justify-content: space-between;
    padding: 0 26px;
  }
  .brand { display: flex; align-items: center; gap: 10px; }
  .brand-dot {
    width: 26px; height: 26px; border-radius: 50%;
    border: 3px solid var(--leaf);
  }
  .brand-name {
    font-family: "Marcellus", Georgia, serif;
    color: var(--leaf);
    font-size: 28px;
  }
  .website {
    font-family: "Marcellus", Georgia, serif;
    color: var(--leaf);
    font-size: 13px;
    letter-spacing: 0.3px;
  }
  .front-body {
    position: absolute; inset: 92px 0 0 0;
    padding: 20px 26px;
    display: flex; justify-content: space-between;
  }
  .person-name {
    font-family: "Marcellus", Georgia, serif;
    color: var(--leaf); font-size: 22px; line-height: 1;
  }
  .person-role { color: var(--leaf); font-size: 11px; margin-top: 3px; }
  .contact-list { list-style: none; margin-top: 18px; }
  .contact-list li {
    display: flex; align-items: center; gap: 10px;
    color: #e8e2dc; font-size: 12.5px; margin-bottom: 9px;
  }
  .contact-list svg { width: 15px; height: 15px; fill: var(--leaf); flex: none; }
  .contact-right { align-self: flex-end; margin-bottom: 14px; position: relative; z-index: 1; }
  .faint-ring {
    position: absolute; right: -34px; bottom: -48px;
    width: 190px; height: 190px; border-radius: 50%;
    border: 14px solid var(--faint);
  }

  /* Back face */
  .card-back {
    background: var(--bark);
    display: flex; flex-direction: column; align-items: center; justify-content: center;
    text-align: center;
  }
  .back-name {
    font-family: "Marcellus", Georgia, serif;
    color: var(--leaf); font-size: 40px; line-height: 1.1;
  }
  .back-tagline {
    font-family: "Alegreya", Georgia, serif;
    color: var(--leaf); font-size: 14px; margin-top: 8px;
  }
</style>
</head>
<body>
  <section class="card card-front" aria-label="Business card front">
    <header class="front-band">
      <div class="brand">
        <span class="brand-dot"></span>
        <span class="brand-name">Roomcraft Willow</span>
      </div>
      <span class="website">www.roomcraftwillow.com</span>
    </header>
    <div class="front-body">
      <div class="contact-left">
        <p class="person-name">Mara Lindqvist</p>
        <p class="person-role">Manager</p>
        <ul class="contact-list">
          <li>
            <svg viewBox="0 0 16 16"><path d="M3 2h3l1 3-2 1.2a8 8 0 0 0 4.8 4.8L11 9l3 1v3a1 1 0 0 1-1 1A12 12 0 0 1 2 3a1 1 0 0 1 1-1z"/></svg>
            (555) 014.2276
          </li>
          <li>
            <svg viewBox="0 0 16 16"><path d="M4.5 1h7a1 1 0 0 1 1 1v12a1 1 0 0 1-1 1h-7a1 1 0 0 1-1-1V2a1 1 0 0 1 1-1zm.5 2v9h6V3zm3 10a.8.8 0 1 0 0 .01z"/></svg>
            (555) 014.9083
          </li>
        </ul>
      </div>
      <ul class="contact-list contact-right">
        <li>
          <svg viewBox="0 0 16 16"><path d="M8 1.5 1 8h2v6.5h4v-4h2v4h4V8h2z"/></svg>
          42 Fernbank Lane, 7310-218
        </li>
        <li>
          <svg viewBox="0 0 16 16"><path d="M1 3.5h14v9H1zm1.5 1.2v.4L8 9l5.5-3.9v-.4zm0 2.2v4.4h11V6.9L8 10.8z"/></svg>
          hello@roomcraftwillow.com
        </li>
      </ul>
      <span class="faint-ring" aria-hidden="true"></span>
    </div>
  </section>

  <section class="card card-back" aria-label="Business card back">
    <p class="back-name">Roomcraft Willow</p>
    <p class="back-tagline">Certified Habitat Vitalis Dwelling Consultant</p>
  </section>
</body>
</html>
```